Vietnamese Restaurant Menu

We are an authentic Vietnamese noodle bar.

We would like our menu redesigned to become more attractive and have a picture for each item. We would like out new menu to look similar to the menu shown on the following website http://quanbepmoc.com.vn/?lang=en

Please find pictures and current menu attached.

If there are any items that you cannot find the pictures for please leave a space and we will add a picture into that slot.

Industry/Entity Type

Restaurant

```html
<!DOCTYPE html>
<html lang="en">
<head>
<meta charset="utf-8">
<title>Noodle Bar Menu</title>
<link href="https://fonts.googleapis.com/css2?family=Cormorant+Garamond:wght@700&family=PT+Sans+Narrow:wght@400;700&display=swap" rel="stylesheet">
<style>
:root{
  --bg:#cbbfa8;
  --page:#f3d891;
  --page-edge:#e9c772;
  --brown:#7d6546;
  --ink:#3d3021;
  --cream:#fff4d6;
  --gold-text:#ffd778;
  --white:#ffffff;
  --red:#d8201c;
}
*{box-sizing:border-box;margin:0;padding:0}
html,body{width:1200px;height:819px;overflow:hidden;background:var(--bg)}
body{font-family:"PT Sans Narrow",sans-serif;color:var(--ink);position:relative}
.page{position:absolute;top:20px;width:580px;height:779px;background:linear-gradient(180deg,var(--page),var(--page-edge));}
.page--left{left:20px;box-shadow:inset -12px 0 18px -12px rgba(0,0,0,.25)}
.page--right{left:600px;box-shadow:inset 12px 0 18px -12px rgba(0,0,0,.25)}
.section-title{position:absolute;left:0;right:0;text-align:center;font-family:"Cormorant Garamond",serif;font-weight:700;font-size:26px;color:var(--ink)}
.section-title span{background:var(--cream);padding:0 14px;border-radius:3px}
.section-sub{position:absolute;left:0;right:0;text-align:center;font-size:11px;font-style:italic;color:var(--ink)}
.photo{position:absolute;border:3px solid var(--white)}
.photo--bowl{background:radial-gradient(circle at 50% 55%,#6d8a3c 0,#a3542b 38%,#2a2420 52%,#e9e1cf 58%,#d9cdb3 100%)}
.photo--soup{background:radial-gradient(circle at 40% 50%,#c99a5a 0,#e8dcc3 30%,#2b2622 48%,#ece6d8 56%,#cfc6b2 100%)}
.photo--red{background:radial-gradient(circle at 55% 55%,#d9452a 0,#b7391f 30%,#3d2a1f 50%,#f2eee6 58%,#e0dacb 100%)}
.photo--drink{background:linear-gradient(180deg,#b06a4e 0,#8f4f3a 45%,#f4ede0 46%,#e8dfcc 70%,#2d2a27 71%,#3a3733 100%)}
.photo--light{background:linear-gradient(180deg,#ffffff,#eee8e2)}
.slot{position:absolute;background:var(--white)}
.card{position:absolute;background:var(--brown);color:var(--cream);padding:7px 9px;font-size:11px;line-height:1.15}
.card--small{font-size:10px;line-height:1.12}
.card b{color:var(--gold-text);font-weight:700}
.card .price{color:var(--gold-text);font-weight:700}
.menu-line{display:flex;justify-content:space-between;gap:8px}
.menu-line .name{color:var(--gold-text);font-weight:700;font-size:12px}
.menu-line .desc{font-size:10px}
.badge{position:absolute;display:flex;align-items:center;gap:4px;font-size:13px;color:var(--ink);font-weight:700;background:var(--cream);padding:2px 6px;border-radius:3px}
.badge i{display:block;width:22px;height:22px;border-radius:50%;background:#5f9d3a}
.tag{position:absolute;background:var(--brown);color:var(--cream);font-size:10px;font-weight:700;text-align:center;line-height:1.1;padding:3px 2px;display:flex;align-items:center;justify-content:center}
.tile{position:absolute;background:var(--white)}
.tile--text{display:flex;align-items:center;justify-content:center;text-align:center;font-weight:700;font-size:12px;color:var(--ink);line-height:1.15}
.burst{position:absolute;width:30px;height:30px;border-radius:50%;background:var(--red)}
</style>
</head>
<body>

<section class="page page--left">
  <h2 class="section-title" style="top:30px"><span>Melody of Entrees</span></h2>
  <p class="section-sub" style="top:66px">A sequence of single notes that is musically satisfying in preparing your palate for an amazing epicurious experience</p>

  <div class="photo photo--bowl" style="left:0;top:88px;width:160px;height:158px" role="img" aria-label="Photo of assorted Vietnamese entrees on a table"></div>
  <div class="badge" style="left:8px;top:100px">all entrees are <i></i></div>
  <div class="card" style="left:160px;top:88px;width:420px;height:158px">
    <div class="menu-line"><div><span class="name">Seafood Spring Rolls</span><br><span class="desc">Shrimp, Crab, Taro, Mushroom, Water Chestnut</span></div><span class="price">(5pcs) 7.80</span></div>
    <div class="menu-line"><div><span class="name">Vegetarian Spring Rolls</span><br><span class="desc">Tofu, Taro, Mushroom, Onion</span></div><span class="price">(5pcs) 7.80</span></div>
    <div class="menu-line"><div><span class="name">Vietnamese Grilled Chicken Cabbage Salad</span><br><span class="desc">Cabbage, Carrots, Vietnamese Mint (Gỏi bắp cải)</span></div><span class="price">8.80</span></div>
    <div class="menu-line"><span class="name">Vietnamese Tofu Mushroom Cabbage Salad</span><span class="price">8.80</span></div>
    <div class="menu-line"><span class="name">Vietnamese Street Food Skewers mixed plate<br>(Marinated Pork skewer + Nem Nuong skewer<br>+ Sugar Cane Prawn)</span><span class="price">8.80</span></div>
  </div>

  <h2 class="section-title" style="top:258px"><span>Symphony of Mains</span></h2>
  <p class="section-sub" style="top:293px">An elaborate musical composition designed to fine-tune even the toughest of tastebuds</p>

  <div class="photo photo--bowl" style="left:60px;top:312px;width:160px;height:150px" role="img" aria-label="Photo of a bowl of beef noodle soup"></div>
  <div class="badge" style="left:70px;top:320px">all mains are <i></i></div>
  <div class="burst" style="left:192px;top:424px;width:34px;height:34px"></div>
  <div class="card" style="left:220px;top:312px;width:350px;height:150px;font-size:10.5px">
    <b>12 hour Vietnamese Beef Noodle Soup Phở Bò</b><br>
    Star Anise fruit, Clove buds, Fennel Seeds, Cardamom pods, Cinnamon quills simmered in a 12 hour beef bone marrow and oxtail broth medium<br>
    <span class="price">13.80 large 15.80</span><br>
    <b>Choice of:</b><br>
    Plain and Simple: Rare Beef Tái<br>
    Adventurous: Rare Beef + Beef Flank Tái Nạm<br>
    Glorious: Rare Beef + Nạm + Bò Viên Beef Balls + Tripe + Tendon<br>
    (Extra $1.50) Đặc biệt
  </div>

  <div class="photo photo--soup" style="left:0;top:476px;width:160px;height:148px" role="img" aria-label="Photo of vegan noodle soup with fried shallots"></div>
  <div class="card card--small" style="left:160px;top:480px;width:130px;height:140px">
    <b>6 hour Vegan Vietnamese Noodle Soup Phở Chay</b><br>
    Star Anise fruit, Clove buds, Fennel Seeds, Cardamom pods, Cinnamon quills simmered in a 6 hour Onion, Pear, Carrot, Apple, Radish and Ginger broth<br>
    <span class="price">medium 13.80 large 15.80</span>
  </div>
  <div class="card card--small" style="left:298px;top:480px;width:140px;height:140px">
    <b>10 hour Central Vietnam Spicy Lemongrass Beef Noodle Bún Bò Huế</b><br>
    Lemongrass, Paprika, Cayenne pepper, Garlic simmered in a 10 hour pork and beef marrow broth drizzled with annatto seed oil<br>
    <span class="price">medium 13.80 large 15.80</span>
  </div>
  <div class="photo photo--red" style="left:440px;top:476px;width:140px;height:148px" role="img" aria-label="Photo of spicy beef noodle soup bowls"></div>

  <div class="photo photo--soup" style="left:0;top:628px;width:160px;height:148px" role="img" aria-label="Photo of chicken noodle soup"></div>
  <div class="card card--small" style="left:160px;top:632px;width:130px;height:140px">
    <b>8 hour Vietnamese Chicken Noodle Soup Phở Gà</b><br>
    Star Anise fruit, Clove buds, Fennel Seeds, Cardamom pods, Cinnamon quills simmered in a 8 hour chicken bone broth<br>
    <span class="price">medium 13.80 large 15.80</span>
  </div>
  <div class="card card--small" style="left:298px;top:632px;width:140px;height:140px">
    <b>10 hour Vietnamese Crab Noodle Soup Bún Riêu</b><br>
    Garlic, Tamarind, Tomato, Onion infused in 10 hour pork marrow, chicken, prawn, and crab broth. Served with melt in your mouth crab and prawn meat balls<br>
    <span class="price">medium 14.80 large 16.80</span>
  </div>
  <div class="photo photo--red" style="left:440px;top:628px;width:140px;height:148px" role="img" aria-label="Photo of crab noodle soup"></div>
</section>

<section class="page page--right">
  <div class="photo photo--bowl" style="left:40px;top:28px;width:140px;height:124px" role="img" aria-label="Photo of vermicelli bowl with spring rolls"></div>
  <div class="card" style="left:180px;top:34px;width:380px;height:112px;font-size:10.5px">
    <b>Vietnamese Vermicelli soup-less wonders</b><br>
    Bún Nem Nướng/ Thịt Nướng<br>
    <span class="price">medium 13.80 large 15.80</span><br>
    <b>Choice of:</b><br>
    Vietnamese Chargrilled Garlic and Roasted Rice Sausage + Seafood Spring Rolls<br>
    Vietnamese Chargrilled Garlic and Roasted Rice Sausage + Marinated Pork Belly<br>
    Marinated Pork Belly + Seafood Spring Roll<br>
    Vegan Tofu + Mushroom · <b>Extra Seafood Spring Rolls / Vegan Spring Rolls 2pcs 2.50</b>
  </div>

  <div class="photo photo--bowl" style="left:30px;top:160px;width:130px;height:112px" role="img" aria-label="Photo of DIY vermicelli roll platter"></div>
  <div class="card card--small" style="left:160px;top:164px;width:128px;height:104px">
    <b>DIY Vietnamese Mixed Meat Vermicelli Rolls with Strings Signature fish sauce 17.50</b><br>
    Gỏi Cuốn. Mix plate of: Vietnamese Chargrilled Sesame and Garlic Pork Sausage, Spring rolls served with fresh herbs
  </div>
  <div class="card card--small" style="left:294px;top:164px;width:128px;height:104px">
    <b>DIY Vietnamese Vegan Salad Vermicelli Rolls with Strings Signature soya sauce 15.80</b><br>
    Gỏi Cuốn Chay. Mix plate of Tofu and mushroom served with fresh herbs
  </div>
  <div class="slot" style="left:428px;top:160px;width:132px;height:112px"></div>

  <h2 class="section-title" style="top:282px;padding-left:60px"><span>Counter Melody Desserts</span></h2>
  <p class="section-sub" style="top:318px;padding-left:60px">A subordinate melody accompanying a principal one that celebrates the journey one has surpassed</p>

  <div class="tag" style="left:40px;top:340px;width:82px;height:40px">Banana Black Bean Sticky Rice and Vanilla Ice Cream 8.80</div>
  <div class="tile" style="left:40px;top:380px;width:82px;height:58px"></div>
  <div class="tag" style="left:127px;top:340px;width:82px;height:40px">Vietnamese tri-coloured dessert Chè ba màu 5.80</div>
  <div class="photo" style="left:127px;top:380px;width:82px;height:58px;background:linear-gradient(160deg,#f5f2ec 0,#c7b39a 50%,#67b36b 100%)" role="img" aria-label="Photo of tri-coloured dessert in glasses"></div>
  <div class="tag" style="left:214px;top:340px;width:82px;height:40px">Orange Mango Sorbet in half an Orange (sm) 4.80</div>
  <div class="tile" style="left:214px;top:380px;width:82px;height:58px"></div>
  <div class="tag" style="left:301px;top:340px;width:82px;height:40px">Lemon Sorbet in half a Lemon (med) 6.80</div>
  <div class="tile" style="left:301px;top:380px;width:82px;height:58px"></div>
  <div class="tag" style="left:388px;top:340px;width:82px;height:40px">Coconut Sorbet in half a Coconut (lrg) 8.80</div>
  <div class="tile" style="left:388px;top:380px;width:82px;height:58px"></div>
  <div class="tag" style="left:475px;top:340px;width:85px;height:40px">Pineapple Sorbet in half a Pineapple (lrg) 8.80</div>
  <div class="tile" style="left:475px;top:380px;width:85px;height:58px"></div>

  <h2 class="section-title" style="top:444px;padding-left:40px"><span>Drinks</span></h2>

  <div class="tag" style="left:40px;top:482px;width:82px;height:28px">Avocado Shake 5.80</div>
  <div class="photo photo--drink" style="left:40px;top:510px;width:82px;height:96px" role="img" aria-label="Photo of avocado shake"></div>
  <div class="tag" style="left:127px;top:482px;width:82px;height:28px">Lychee Shake 5.80</div>
  <div class="photo photo--light" style="left:127px;top:510px;width:82px;height:96px" role="img" aria-label="Photo of lychee shake with lychees"></div>
  <div class="tag" style="left:214px;top:482px;width:82px;height:28px">Jackfruit Shake 5.80</div>
  <div class="photo photo--drink" style="left:214px;top:510px;width:82px;height:96px" role="img" aria-label="Photo of jackfruit shake"></div>
  <div class="tag" style="left:301px;top:482px;width:82px;height:28px">Mango Shake 5.80</div>
  <div class="tile" style="left:301px;top:510px;width:82px;height:96px"></div>
  <div class="tag" style="left:388px;top:482px;width:82px;height:28px">Watermelon Shake 5.80</div>
  <div class="tile" style="left:388px;top:510px;width:82px;height:96px"></div>
  <div class="tag" style="left:475px;top:482px;width:85px;height:28px">Vietnamese Ice Coffee 4.50</div>
  <div class="tile" style="left:475px;top:510px;width:85px;height:96px"></div>
  <div class="burst" style="left:548px;top:526px"></div>

  <div class="tag" style="left:90px;top:622px;width:84px;height:28px">Coconut Juice 4.50</div>
  <div class="photo photo--drink" style="left:90px;top:650px;width:84px;height:100px" role="img" aria-label="Photo of coconut juice"></div>
  <div class="tag" style="left:179px;top:622px;width:84px;height:28px">Soft Drink - Cola,</div>
  <div class="tile tile--text" style="left:179px;top:650px;width:84px;height:100px">Cola Zero,<br>Lemon Fizz,<br>Orange Fizz,<br>Passion Fizz,<br>Creaming Soda<br>3.80</div>
  <div class="tag" style="left:268px;top:622px;width:84px;height:28px">Apple Juice, Orange Juice 3.80</div>
  <div class="photo photo--drink" style="left:268px;top:650px;width:84px;height:100px" role="img" aria-label="Photo of juice glass"></div>
  <div class="tag" style="left:357px;top:622px;width:84px;height:28px">Mineral Water 2.80</div>
  <div class="photo photo--drink" style="left:357px;top:650px;width:84px;height:100px" role="img" aria-label="Photo of mineral water glass"></div>
  <div class="tag" style="left:446px;top:622px;width:90px;height:28px">Specialised Tea</div>
  <div class="tile tile--text" style="left:446px;top:650px;width:90px;height:100px">Green Tea<br>Jasmine,<br>Green Tea,<br>Oolong Tea,<br>Pandan Tea,<br>Lotus Tea<br>3.50</div>
</section>

</body>
</html>
```